I need a book cover designed for my book entitled Ten Small Shifts ~ The Lacquer Diary --- This book

I need a book cover designed for this book. I envision the book size being 6x6. This book will take the reader, week by week, over the course of a year, into my journey of going bold through the weekly changing of my nail polish color. The book will contain pictures of the nail polish colors as well as weekly journal entries, monthly summaries and then an overall conlusion that detail the personal discovery and growth that took place through this simple, yet consistent practice of going bold by changing my nail polish.

Reason: I would like to extend the deadline by five days because I have several people looking at the designs and providing their thoughts and a few people have been unable to do so this week! Thank you SO much! Dora :)

```html
<!DOCTYPE html>
<html lang="en">
<head>
<meta charset="utf-8">
<title>Ten Small Shifts ~ The Lacquer Diary</title>
<link rel="stylesheet" href="https://fonts.googleapis.com/css2?family=Anton&family=Dancing+Script:wght@600&display=swap">
<style>
  :root {
    --paper: #ffffff;
    --title-magenta: #c000e0;
    --script-lilac: #d57fea;
    --skin-light: #f3d2bf;
    --skin-mid: #e6b59c;
    --nail-pink: #d94fb0;
    --nail-teal: #3fb3b8;
    --nail-yellow: #f2cf3a;
    --nail-red: #e2413c;
  }
  html, body {
    margin: 0;
    padding: 0;
    overflow: hidden;
    background: var(--paper);
  }
  .cover {
    position: relative;
    width: 1200px;
    height: 1200px;
    overflow: hidden;
    background: var(--paper);
  }
  .hands-frame {
    position: absolute;
    inset: 0;
    width: 1200px;
    height: 1200px;
  }
  .title-block {
    position: absolute;
    left: 0;
    right: 0;
    top: 345px;
    text-align: center;
  }
  .title-bold {
    margin: 0;
    font-family: "Anton", "Impact", sans-serif;
    font-size: 132px;
    line-height: 1.02;
    letter-spacing: 1px;
    color: var(--title-magenta);
    text-transform: uppercase;
  }
  .title-script {
    margin: 14px 0 0;
    font-family: "Dancing Script", cursive;
    font-weight: 600;
    font-size: 108px;
    line-height: 0.95;
    color: var(--script-lilac);
  }
</style>
</head>
<body>
  <main class="cover">
    <svg class="hands-frame" viewBox="0 0 1200 1200" role="img"
         aria-label="Photograph of many hands with glossy painted nails in bright colours, arranged in a ring forming a heart around the title">
      <defs>
        <radialGradient id="handsTone" cx="50%" cy="50%" r="70%">
          <stop offset="45%" stop-color="var(--skin-light)"/>
          <stop offset="65%" stop-color="var(--skin-mid)"/>
          <stop offset="100%" stop-color="var(--skin-light)"/>
        </radialGradient>
        <linearGradient id="nailTint" x1="0" y1="0" x2="1" y2="1">
          <stop offset="0%" stop-color="var(--nail-pink)" stop-opacity="0.35"/>
          <stop offset="35%" stop-color="var(--nail-teal)" stop-opacity="0.3"/>
          <stop offset="65%" stop-color="var(--nail-yellow)" stop-opacity="0.3"/>
          <stop offset="100%" stop-color="var(--nail-red)" stop-opacity="0.35"/>
        </linearGradient>
      </defs>
      <path fill-rule="evenodd" fill="url(#handsTone)"
        d="M0 0 H1200 V1200 H0 Z
           M600 300 C520 180 120 160 110 430 C100 700 420 900 600 1130 C780 900 1100 700 1090 430 C1080 160 680 180 600 300 Z"/>
      <path fill-rule="evenodd" fill="url(#nailTint)"
        d="M0 0 H1200 V1200 H0 Z
           M600 300 C520 180 120 160 110 430 C100 700 420 900 600 1130 C780 900 1100 700 1090 430 C1080 160 680 180 600 300 Z"/>
    </svg>

    <header class="title-block">
      <h1 class="title-bold">Ten Small<br>Shifts</h1>
      <p class="title-script">The Lacquer<br>Diary</p>
    </header>
  </main>
</body>
</html>
```